Velvor Display PowerPoint Design Project

We need PowerPoint slide templates for our Sales Media Kit at our re-branded company based in Canada called "Velvor Display Collective".

Looking for a look that clearly and powerfully portrays our unique and effective indoor advertising billboards in our network.

Our TinyPanes, WideSlats and GrandSheets are strategically placed in high traffic areas of restaurants, pubs, nightclubs, fitness clubs, colleges and universities, and sports arenas.

Key features of our media is a captive audience and 100% gender specific.

You can visit our old website for info on the above three media products (plorvex.ca)

Our Media Kits go out to small, medium business owners and advertising agenices.

Deliverables are:

1) Presentation cover slide with rich graphic content and space for content.
2) Presentation body slide with room for content 2 photos or logos. This slide should have the following:
a) No graphic in the text area
b) Space for page number at the bottom.
3) Photoshop (PSD) files for all graphic elements.
4) Font files for all fonts used.

Project Deadline Extended
Reason: Need more designs submitted.

We have uploaded our business card file.

Would like to incorporate the look, feel and colour of our business card to the power point template.

Target Market(s)

small business owners, marketing managers, media buyers and advertising agencies.

Industry/Entity Type

Advertising

Requirements
Must have
• We would like to see designs that:
- use the color scheme indicated by the attached logo design, perhaps expanding on it slightly.
- Look should be professional, smooth, and colourful.
-Must have a clean and modern feel that Ad Agencies would be impressed with.
-We have uploaded our business card file.

-Would like to incorporate the look, feel and colour of our business card to the power point template.

```html
<!DOCTYPE html>
<html lang="en">
<head>
<meta charset="utf-8">
<title>Velvor Display Collective – Slide Template Set</title>
<link href="https://fonts.googleapis.com/css2?family=Source+Sans+3:ital,wght@0,400;0,600;0,700;1,700&family=Alfa+Slab+One&display=swap" rel="stylesheet">
<style>
:root{
  --stage:#c48a55;
  --paper:#ffffff;
  --brand-blue:#2a6ab4;
  --text-grey:#8a8a8a;
  --rule:#e2e2e2;
  --table-head:#6e6e6e;
  --cyl:#7d7d7d;
  --thanks-grey:#6b6b6b;
  --photo-sign-a:#3f6f4e;
  --photo-sign-b:#c9b27a;
  --photo-man-a:#3a2c26;
  --photo-man-b:#8a6a58;
  --photo-ad-a:#f3f1ea;
  --photo-ad-b:#cfd8c4;
}
*{box-sizing:border-box;margin:0;padding:0}
html,body{width:1200px;height:687px;overflow:hidden}
body{background:var(--stage);font-family:"Source Sans 3",Arial,sans-serif;position:relative}
.slide{position:absolute;width:237px;height:177px;background:var(--paper);box-shadow:0 2px 5px rgba(0,0,0,.25);overflow:hidden}
.slide-footer{position:absolute;left:0;right:0;bottom:0;height:19px;background:var(--brand-blue);color:#fff;font-size:5.5px;font-weight:700;font-style:italic;line-height:19px;padding-left:14px}
.page-number{position:absolute;right:6px;bottom:2px;width:20px;height:20px;border-radius:50%;background:var(--paper);color:#222;font-size:9px;line-height:20px;text-align:center}
.brand{position:absolute;left:0;right:0;text-align:center;color:var(--brand-blue);font-weight:700;font-size:26px;line-height:1;letter-spacing:.3px}
.slide-title{position:absolute;color:var(--brand-blue);font-weight:700;font-size:9.5px;letter-spacing:.2px;white-space:nowrap}
.body-copy{position:absolute;color:var(--text-grey);font-size:4.3px;line-height:6.2px}
.bullets{position:absolute;list-style:none}
.bullets li{position:relative;padding-left:7px;white-space:nowrap}
.bullets li::before{content:"";position:absolute;left:0;top:2.3px;width:2.6px;height:2.6px;border-radius:50%;background:var(--brand-blue)}
.bullets-blue li{color:var(--brand-blue);font-weight:700;font-size:4.8px;line-height:10.5px}
.bullets-grey li{color:var(--text-grey);font-size:4.3px;line-height:14px}
.bullets-grey li::before{top:5.5px}
.photo{position:absolute}
.photo-sign{background:linear-gradient(180deg,var(--photo-sign-a),var(--photo-sign-b) 60%,#6b6b6b)}
.photo-man{background:linear-gradient(160deg,var(--photo-man-a),var(--photo-man-b))}
.photo-ad{background:linear-gradient(160deg,var(--photo-ad-a),var(--photo-ad-b));border:2px solid #333}
.part-heading{position:absolute;left:0;right:0;top:76px;text-align:center;color:var(--brand-blue);font-weight:700;font-size:15px}
.data-table{position:absolute;left:28px;top:42px;width:176px;border-collapse:collapse;font-size:4.2px;color:var(--text-grey)}
.data-table th{background:var(--table-head);color:#fff;font-size:6.5px;font-weight:700;height:15px}
.data-table td{height:12px;padding-left:8px;border-bottom:1px solid var(--rule);background:#fafafa}
.sub-list{position:absolute;list-style:none;width:98px}
.sub-list li{position:relative;padding-left:6px;margin-bottom:7px;font-size:4.2px;line-height:6px;color:var(--text-grey);white-space:nowrap}
.sub-list li::before{content:"";position:absolute;left:0;top:2px;width:2.4px;height:2.4px;border-radius:50%;background:var(--brand-blue)}
.sub-list .sub-title{color:var(--brand-blue)}
.thanks{position:absolute;left:0;right:0;top:100px;text-align:center;font-family:"Alfa Slab One",Georgia,serif;font-size:14px;color:var(--thanks-grey)}
.thanks-sub{position:absolute;left:0;right:0;top:118px;text-align:center;font-weight:700;font-size:8px;color:var(--brand-blue)}
</style>
</head>
<body>

<section class="slide" style="left:367px;top:58px">
  <div class="brand" style="top:22px">Velvor</div>
  <h1 class="slide-title" style="left:0;right:0;top:86px;text-align:center;font-size:12px">TITLE OF PRESENTATION</h1>
  <footer class="slide-footer">www.velvordisplaycollective.com</footer><span class="page-number">1</span>
</section>

<section class="slide" style="left:635px;top:58px">
  <h2 class="slide-title" style="left:40px;top:13px">LOREM IPSUM&nbsp; LOREM</h2>
  <p class="body-copy" style="left:40px;top:40px;width:162px">Lorem ipsum dolor sit amet, consectetuer adipiscing elit, sed diam nonummy nibh euismod tincidunt ut laoreet dolore magna aliquam erat volutpat. Ut wisi enim ad minim veniam, quis nostrud exerci tation ullamcorper suscipit lobortis nisl ut aliquip ex ea commodo consequat. Duis autem vel eum iriure dolor in hendrerit in vulputate velit esse molestie.</p>
  <ul class="bullets bullets-blue" style="left:40px;top:90px">
    <li>Lorem ipsum Lorem Lorem ipsum Lorem</li>
    <li>Lorem ipsum Lorem Lorem</li>
    <li>Lorem ipsum Lorem Lorem ipsum Lorem Lorem ipsum</li>
    <li>Lorem ipsum orem Lorem ipsum Lo</li>
    <li>Lorem ipsum Lorem</li>
  </ul>
  <footer class="slide-footer">www.velvordisplaycollective.com</footer><span class="page-number">2</span>
</section>

<section class="slide" style="left:902px;top:58px">
  <h2 class="slide-title" style="left:14px;top:13px">LOREM IPSUM&nbsp; LOREM</h2>
  <p class="body-copy" style="left:14px;top:32px;width:108px">Lorem ipsum dolor sit amet, consectetuer adipiscing elit, sed diam nonummy nibh euismod tincidunt ut laoreet dolore magna aliquam erat volutpat. Ut wisi enim ad minim veniam, quis nostrud exerci tation ullamcorper suscipit lobortis nisl ut aliquip ex ea commodo consequat.</p>
  <p class="body-copy" style="left:14px;top:94px;width:108px">Lorem ipsum dolor sit amet, consectetuer adipiscing elit, sed diam nonummy nibh euismod tincidunt ut laoreet dolore magna aliquam erat volutpat. Ut wisi enim ad minim veniam, quis nostrud exerci tation ullamcorper suscipit lobortis nisl ut aliquip ex ea commodo.</p>
  <div class="photo photo-sign" role="img" aria-label="Photo of an outdoor digital roadside sign" style="left:128px;top:15px;width:88px;height:127px"></div>
  <footer class="slide-footer">www.velvordisplaycollective.com</footer><span class="page-number">3</span>
</section>

<section class="slide" style="left:63px;top:247px">
  <div class="brand" style="top:20px">Velvor</div>
  <h2 class="part-heading">PART 3</h2>
  <p class="body-copy" style="left:60px;top:102px;width:120px;text-align:center">Lorem ipsum dolor sit amet, consectetuer adipiscing elit, sed diam nonummy nibh euismod tincidunt ut laoreet dolore magna aliquam erat volutpat. Ut wisi enim ad minim veniam, quis nos.</p>
  <footer class="slide-footer">www.velvordisplaycollective.com</footer><span class="page-number">4</span>
</section>

<section class="slide" style="left:367px;top:247px">
  <h2 class="slide-title" style="left:11px;top:14px">LOREM IPSUM</h2>
  <p class="body-copy" style="left:11px;top:31px;width:214px">Lorem ipsum dolor sit amet, consectetuer adipiscing elit, sed diam nonummy nibh euismod tincidunt ut laoreet dolore magna aliquam erat volutpat. Ut wisi enim ad minim veniam, quis nostrud exerci tation ullamcorper suscipit lobortis nisl ut aliquip ex ea commodo consequat. Duis autem vel eum iriure.</p>
  <div class="photo photo-man" role="img" aria-label="Photo of an indoor advertising poster" style="left:11px;top:69px;width:52px;height:70px"></div>
  <p class="body-copy" style="left:74px;top:69px;width:84px">Lorem ipsum dolor sit amet, consectetuer adipiscing elit, sed diam nonummy nibh euismod tincidunt ut laoreet dolore magna aliquam erat volutpat. Ut wisi enim ad minim veniam, quis nostrud exerci tation ullamcorper suscipit lobortis nisl ut aliquip ex ea commodo consequat.</p>
  <div class="photo photo-ad" role="img" aria-label="Framed print advertisement with a bird illustration" style="left:163px;top:69px;width:57px;height:70px"></div>
  <footer class="slide-footer">www.velvordisplaycollective.com</footer><span class="page-number">5</span>
</section>

<section class="slide" style="left:635px;top:247px">
  <h2 class="slide-title" style="left:38px;top:13px">LOREM IPSUM</h2>
  <table class="data-table">
    <thead><tr><th colspan="4">Lorem ipsum&nbsp; Lorem ipsum&nbsp; Lorem ipsum</th></tr></thead>
    <tbody>
      <tr><td>Lorem ipsum</td><td>Lorem ipsum</td><td>Lorem ipsum</td><td>Lorem ipsum</td></tr>
      <tr><td>Lorem ipsum</td><td>Lorem ipsum</td><td>Lorem ipsum</td><td>Lorem ipsum</td></tr>
      <tr><td>Lorem ipsum</td><td>Lorem ipsum</td><td>Lorem ipsum</td><td>Lorem ipsum</td></tr>
      <tr><td>Lorem ipsum</td><td>Lorem ipsum</td><td>Lorem ipsum</td><td>Lorem ipsum</td></tr>
      <tr><td>Lorem ipsum</td><td>Lorem ipsum</td><td>Lorem ipsum</td><td>Lorem ipsum</td></tr>
      <tr><td>Lorem ipsum</td><td>Lorem ipsum</td><td>Lorem ipsum</td><td>Lorem ipsum</td></tr>
      <tr><td>Lorem ipsum</td><td>Lorem ipsum</td><td>Lorem ipsum</td><td>Lorem ipsum</td></tr>
      <tr><td>Lorem ipsum</td><td>Lorem ipsum</td><td>Lorem ipsum</td><td>Lorem ipsum</td></tr>
    </tbody>
  </table>
  <footer class="slide-footer">www.velvordisplaycollective.com</footer><span class="page-number">6</span>
</section>

<section class="slide" style="left:902px;top:247px">
  <h2 class="slide-title" style="left:24px;top:13px">LOREM IPSUM</h2>
  <svg class="flow-diagram" width="237" height="158" viewBox="0 0 237 158" style="position:absolute;left:0;top:0" font-family="Source Sans 3, Arial, sans-serif">
    <g stroke="#c8c8c8" stroke-width="0.8" fill="none">
      <path d="M21 50 H17 V98 H22 M17 73 H22"/>
      <path d="M63 50 H59 V125 H64 M59 73 H64 M59 99 H64"/>
      <path d="M106 50 H102 V125 H107 M102 73 H107 M102 99 H107"/>
      <path d="M149 50 H145 V125 H150 M145 73 H150 M145 99 H150"/>
    </g>
    <g fill="var(--brand-blue)">
      <rect x="21" y="42" width="36" height="14" rx="1.5"/>
      <rect x="63" y="42" width="36" height="14" rx="1.5"/>
      <rect x="106" y="42" width="36" height="14" rx="1.5"/>
      <rect x="149" y="42" width="36" height="14" rx="1.5"/>
    </g>
    <g fill="#fff" font-size="4.3" font-weight="700" text-anchor="middle">
      <text x="39" y="50.5">Lorem ipsum</text><text x="81" y="50.5">Lorem ipsum</text>
      <text x="124" y="50.5">Lorem ipsum</text><text x="167" y="50.5">Lorem ipsum</text>
    </g>
    <g fill="var(--cyl)" stroke="#fff" stroke-width="0.6">
      <path d="M22 66 a12 3 0 0 1 24 0 v14 a12 3 0 0 1 -24 0 z"/>
      <path d="M22 92 a12 3 0 0 1 24 0 v14 a12 3 0 0 1 -24 0 z"/>
      <path d="M64 66 a12 3 0 0 1 24 0 v14 a12 3 0 0 1 -24 0 z"/>
      <path d="M64 92 a12 3 0 0 1 24 0 v14 a12 3 0 0 1 -24 0 z"/>
      <path d="M64 118 a12 3 0 0 1 24 0 v14 a12 3 0 0 1 -24 0 z"/>
      <path d="M107 66 a12 3 0 0 1 24 0 v14 a12 3 0 0 1 -24 0 z"/>
      <path d="M107 92 a12 3 0 0 1 24 0 v14 a12 3 0 0 1 -24 0 z"/>
      <path d="M107 118 a12 3 0 0 1 24 0 v14 a12 3 0 0 1 -24 0 z"/>
      <path d="M150 66 a12 3 0 0 1 24 0 v14 a12 3 0 0 1 -24 0 z"/>
      <path d="M150 92 a12 3 0 0 1 24 0 v14 a12 3 0 0 1 -24 0 z"/>
      <path d="M150 118 a12 3 0 0 1 24 0 v14 a12 3 0 0 1 -24 0 z"/>
    </g>
    <g fill="#fff" font-size="4.3" font-weight="600" text-anchor="middle">
      <text x="34" y="75">Lorem</text><text x="34" y="101">Lorem</text>
      <text x="76" y="75">Lorem</text><text x="76" y="101">Lorem</text><text x="76" y="127">Lorem</text>
      <text x="119" y="75">Lorem</text><text x="119" y="101">Lorem</text><text x="119" y="127">Lorem</text>
      <text x="162" y="75">Lorem</text><text x="162" y="101">Lorem</text><text x="162" y="127">Lorem</text>
    </g>
  </svg>
  <footer class="slide-footer">www.velvordisplaycollective.com</footer><span class="page-number">7</span>
</section>

<section class="slide" style="left:367px;top:452px">
  <h2 class="slide-title" style="left:14px;top:13px">LOREM IPSUM</h2>
  <ul class="bullets bullets-grey" style="left:14px;top:44px">
    <li>Lorem ipsum dolor sit amet, consectetuer adipiscing elit, sed diam nonummy</li>
    <li>Lorem ipsum dolor sit amet, consectetuer adipiscing elit, sed diam nonummy</li>
    <li>Lorem ipsum dolor sit amet, consectetuer adipiscing elit, sed diam nonummy</li>
    <li>Lorem ipsum dolor sit amet, consectetuer adipiscing elit, sed diam nonummy</li>
    <li>Lorem ipsum dolor sit amet, consectetuer adipiscing elit, sed diam nonummy</li>
    <li>Lorem ipsum dolor sit amet, consectetuer.</li>
  </ul>
  <footer class="slide-footer">www.velvordisplaycollective.com</footer><span class="page-number">8</span>
</section>

<section class="slide" style="left:635px;top:452px">
  <h2 class="slide-title" style="left:14px;top:13px">LOREM IPSUM</h2>
  <ul class="sub-list" style="left:14px;top:42px">
    <li><span class="sub-title">Sub Title-1</span><br>Lorem ipsum dolor sit amet, eiuer.<br>Adipiscing elit, sed diam non euismod</li>
    <li><span class="sub-title">Sub Title-2</span><br>Lorem ipsum dolor sit amet, eiuer.<br>Adipiscing elit, sed diam non rimod tinci</li>
    <li><span class="sub-title">Sub Title-3</span><br>Lorem ipsum dolor sit amet, eiuer.<br>Adipiscing elit, nummy nibh euismod</li>
  </ul>
  <ul class="sub-list" style="left:122px;top:42px">
    <li><span class="sub-title">Sub Title-1</span><br>Lorem ipsum dolor sit amet, consectetuer</li>
    <li><span class="sub-title">Sub Title-2</span><br>Lorem ipsum dolor sit amet, consectetuer<br>Adipiscing elit, nonummy nibh euismod</li>
    <li><span class="sub-title">Sub Title-3</span><br>Lorem ipsum dolor sit amet, consectetuer<br>Adipiscing elit, nonummy nibh euismod</li>
  </ul>
  <footer class="slide-footer">www.velvordisplaycollective.com</footer><span class="page-number">9</span>
</section>

<section class="slide" style="left:902px;top:452px">
  <div class="brand" style="top:22px">Velvor</div>
  <p class="thanks">Thank You!</p>
  <p class="thanks-sub">For your attention</p>
  <footer class="slide-footer">www.velvordisplaycollective.com</footer><span class="page-number">10</span>
</section>

</body>
</html>
```